Corporate Branding - Web and Print

A UK based company will like to use an existing logo to create branding materials for all marketing related documents, including business card, prints, letterhead, Website, Twitter, Facebook, Instagram logo etc. This company serves high-end clientele in the fashion, health and wellness and as such high quality and class is of utmost importance.
Where the logo can be modernised without losing its character then experiment. The main thing is to have a corporate branding which can be used later for brochures, Business Plan infographics.
The prominent colour within the organisation is burnt orange with no secondary colour. However if you believe a secondary colour is needed then use it, otherwise keep it simple and classy. Any chosen colours have to match perfectly.
Target Market(s)
High net worth individuals
Industry/Entity Type
Health And Wellness
Contact Information for Business Card
classy
Look and feel
Each slider illustrates characteristics of the customer's brand and the style your logo design should communicate.

```html
<!DOCTYPE html>
<html lang="en">
<head>
<meta charset="utf-8">
<title>Velora Business Card</title>
<link rel="stylesheet" href="https://fonts.googleapis.com/css2?family=Montserrat:wght@600;700;800&display=swap">
<style>
  :root {
    --surface: #ececec;
    --card-light: #f2f3f0;
    --card-dark: #2e322f;
    --band-dark: #2a2c2b;
    --burnt-orange: #f08c1e;
    --accent-blue: #1f3fa8;
    --ink: #2f2f2f;
    --mark-faint: #d2d2d0;
  }
  * { margin: 0; padding: 0; box-sizing: border-box; }
  html, body { width: 1029px; height: 1200px; overflow: hidden; }
  body {
    background: var(--surface);
    font-family: "Montserrat", sans-serif;
    position: relative;
  }
  .card {
    position: absolute;
    left: 134px;
    width: 760px;
    height: 440px;
    overflow: hidden;
  }
  .card--front { top: 110px; background: var(--card-light); }
  .card--back { top: 650px; background: var(--card-dark); }

  .band { position: absolute; left: 0; right: 0; height: 34px; background: var(--band-dark); }
  .band--top { top: 0; border-bottom: 4px solid var(--burnt-orange); }
  .band--bottom { bottom: 0; border-top: 4px solid var(--burnt-orange); }

  .faint-mark {
    position: absolute;
    right: 90px;
    top: 70px;
    width: 190px;
    height: 190px;
    border-radius: 50%;
    background: var(--mark-faint);
  }

  .contact { position: absolute; left: 58px; top: 70px; color: var(--ink); font-weight: 700; }
  .contact__name { color: var(--burnt-orange); font-size: 36px; line-height: 1.1; letter-spacing: 0.5px; }
  .contact__role { color: var(--accent-blue); font-size: 18px; margin-bottom: 14px; }
  .contact__group { font-size: 22px; line-height: 1.2; margin-bottom: 14px; }

  .guide-line {
    position: absolute; left: 0; right: 0; height: 3px;
    background: var(--burnt-orange);
  }
  .guide-line--top { top: 30px; }
  .guide-line--bottom { bottom: 30px; }

  .brand {
    position: absolute; inset: 0;
    display: flex; align-items: center; justify-content: center; gap: 26px;
  }
  .brand__dot { width: 100px; height: 100px; border-radius: 50%; background: var(--burnt-orange); }
  .brand__name {
    color: var(--burnt-orange);
    font-size: 96px;
    font-weight: 800;
    letter-spacing: 4px;
  }
</style>
</head>
<body>
  <section class="card card--front" aria-label="Business card front">
    <div class="band band--top"></div>
    <div class="faint-mark"></div>
    <div class="contact">
      <p class="contact__name">Daniel R. Hartley</p>
      <p class="contact__role">Founder</p>
      <div class="contact__group">
        <p>Address line 001</p>
        <p>Adsress line 002</p>
      </div>
      <div class="contact__group">
        <p>07700 900481</p>
        <p>555-318-0427</p>
        <p>555-764-1190</p>
      </div>
      <div class="contact__group">
        <p>hello@danielhartley.com</p>
        <p>danielhartley.com</p>
      </div>
    </div>
    <div class="band band--bottom"></div>
  </section>

  <section class="card card--back" aria-label="Business card back">
    <div class="guide-line guide-line--top"></div>
    <div class="brand">
      <div class="brand__dot"></div>
      <p class="brand__name">VELORA</p>
    </div>
    <div class="guide-line guide-line--bottom"></div>
  </section>
</body>
</html>
```